I am looking for help designing my new business cards. I would like rounded edges and a raised logo on the back of the card. I have 2 Logos. One with a boat in it and one without. I'd like the one on the back to be the one that includes the boat and just the name on the front. I have included multiple formats of my logo. Please let me know if you need anymore.

Target Market(s)

Potential buyers and other sales brokers

Industry/Entity Type

Sales - Yacht / Boat Sales

Contact Information for Business Card

Id liike the front to include just the business name portion of the logo along with my name (Corwin Dalby), phone number (555.318.6027), website address (www.dalbymarineco.example) and not my physical address but just "Wrenhaven, SC". The back should include my full logo that has the boat included. This portion I'd prefer raised amd take up the majority of the space there. Thanks!!

Colors
0054AA
0677BA
7BADD7
CADEEF
E8F1F8
0094D4
00A9DD
6FCCEA
C7EBF8
E9F6FB

Requirements
Must have
• Double sided
Nice to have
• My email address: Corwin@dalbymarineco.example The NMTG logo somewhere small on the front of the card
Should not have
• My full address, prefer only "Wrenhaven, SC"

```html
<!DOCTYPE html>
<html lang="en">
<head>
<meta charset="utf-8">
<title>Dalby Marine Co — Business Card</title>
<link rel="stylesheet" href="https://fonts.googleapis.com/css2?family=Montserrat:wght@400;500;700;800&display=swap">
<style>
  :root {
    --stage: #2e2e30;
    --navy: #0b2d6e;
    --navy-deep: #062660;
    --blue: #0677ba;
    --sky: #0094d4;
    --paper: #ffffff;
    --ink: #1d1d24;
  }
  * { box-sizing: border-box; margin: 0; padding: 0; }
  html, body { width: 1200px; height: 689px; overflow: hidden; }
  body {
    background: var(--stage);
    font-family: "Montserrat", sans-serif;
    position: relative;
  }
  .card {
    position: absolute;
    top: 190px;
    width: 540px;
    height: 309px;
    border-radius: 24px;
    overflow: hidden;
    box-shadow: 0 18px 40px rgba(0,0,0,.45);
  }
  /* Back of card */
  .card--back { left: 30px; }
  .back-art {
    position: absolute; inset: 0;
    background: linear-gradient(160deg, #0a6fb0 0%, #06428c 40%, var(--navy-deep) 100%);
  }
  .back-logo {
    position: absolute; inset: 0;
    display: flex; flex-direction: column; align-items: center; justify-content: center;
    color: var(--paper);
  }
  .back-logo .brand-name {
    font-weight: 800; font-size: 46px; letter-spacing: 2px; line-height: 1;
  }
  .back-logo .brand-rule {
    margin-top: 12px; width: 300px; height: 2px; background: var(--paper);
  }
  /* Front of card */
  .card--front { left: 630px; background: var(--paper); }
  .front-logo {
    position: absolute; left: 28px; top: 120px;
    display: flex; align-items: center; gap: 10px;
    color: var(--navy);
  }
  .front-logo .brand-mark { width: 14px; height: 14px; background: var(--blue); }
  .front-logo .brand-name {
    font-weight: 800; font-size: 22px; letter-spacing: 1px; line-height: 1.05;
  }
  .divider {
    position: absolute; left: 250px; top: 40px; width: 1px; height: 180px;
    background: linear-gradient(180deg, rgba(0,0,0,0), rgba(0,0,0,.35) 40%, rgba(0,0,0,.35) 60%, rgba(0,0,0,0));
  }
  .contact { position: absolute; left: 272px; top: 52px; color: var(--ink); }
  .contact .person {
    font-weight: 500; font-size: 19px; letter-spacing: 2px; text-transform: uppercase;
    color: var(--navy); margin-bottom: 14px;
  }
  .contact ul { list-style: none; }
  .contact li {
    display: flex; align-items: center; gap: 9px;
    font-size: 12.5px; font-weight: 400; line-height: 1; margin-bottom: 10px;
  }
  .contact li svg { width: 13px; height: 13px; fill: var(--navy); flex: none; }
  .contact .web-accent { color: var(--blue); }
  .band-stripe { position: absolute; left: 0; right: 0; bottom: 26px; height: 5px; background: var(--blue); }
  .band-base { position: absolute; left: 0; right: 0; bottom: 0; height: 26px; background: var(--navy-deep); }
</style>
</head>
<body>
  <section class="card card--back" aria-label="Card back">
    <div class="back-art" role="img" aria-label="Blue gradient background with a faint boat illustration"></div>
    <div class="back-logo">
      <span class="brand-name">DALBY MARINE CO</span>
      <span class="brand-rule"></span>
    </div>
  </section>

  <section class="card card--front" aria-label="Card front">
    <div class="front-logo">
      <span class="brand-mark"></span>
      <span class="brand-name">DALBY<br>MARINE CO</span>
    </div>
    <div class="divider"></div>
    <div class="contact">
      <p class="person">Corwin Dalby</p>
      <ul>
        <li>
          <svg viewBox="0 0 24 24"><path d="M6.6 10.8a15.1 15.1 0 0 0 6.6 6.6l2.2-2.2a1 1 0 0 1 1-.25 11.4 11.4 0 0 0 3.6.57 1 1 0 0 1 1 1V20a1 1 0 0 1-1 1A17 17 0 0 1 3 4a1 1 0 0 1 1-1h3.5a1 1 0 0 1 1 1c0 1.25.2 2.46.57 3.6a1 1 0 0 1-.25 1z"/></svg>
          555.318.6027
        </li>
        <li>
          <svg viewBox="0 0 24 24"><path d="M2 5h20v14H2zM4 7v.5l8 5 8-5V7l-8 5z"/></svg>
          Corwin@dalbymarineco.example
        </li>
        <li>
          <svg viewBox="0 0 24 24"><path d="M12 2a10 10 0 1 0 0 20 10 10 0 0 0 0-20zm0 2c.9 1.2 1.6 2.6 2 4h-4c.4-1.4 1.1-2.8 2-4zM4.3 14a8 8 0 0 1 0-4h3.4a16 16 0 0 0 0 4zm.8 2h3c.3 1.3.8 2.5 1.4 3.6A8 8 0 0 1 5.1 16zm3-8h-3a8 8 0 0 1 4.4-3.6C8.9 5.5 8.4 6.7 8.1 8zM12 20c-.9-1.2-1.6-2.6-2-4h4c-.4 1.4-1.1 2.8-2 4zm2.3-6H9.7a14 14 0 0 1 0-4h4.6a14 14 0 0 1 0 4zm.2 5.6c.6-1.1 1.1-2.3 1.4-3.6h3a8 8 0 0 1-4.4 3.6zM16.3 14a16 16 0 0 0 0-4h3.4a8 8 0 0 1 0 4z"/></svg>
          <span>www.<span class="web-accent">dalbymarineco</span>.example</span>
        </li>
        <li>
          <svg viewBox="0 0 24 24"><path d="M12 2a7 7 0 0 0-7 7c0 5.2 7 13 7 13s7-7.8 7-13a7 7 0 0 0-7-7zm0 9.5A2.5 2.5 0 1 1 12 6.5a2.5 2.5 0 0 1 0 5z"/></svg>
          Wrenhaven, SC
        </li>
      </ul>
    </div>
    <div class="band-stripe"></div>
    <div class="band-base"></div>
  </section>
</body>
</html>
```